Voyage Wellness Point Business Cards

We need business cards for our new start-up online travel health clinic. Visit our website voyagewellpoint.ca for branding and more info.

Target Market(s)

Travellers

Industry/Entity Type

Business

Contact Information for Business Card

Mara Kowalczyk
mara@voyagewellpoint.ca
+1 555 283 0461
voyagewellpoint.ca

Font styles to use
Sans Serif

Colors
f68d4d

```html
<!DOCTYPE html>
<html lang="en">
<head>
<meta charset="utf-8">
<title>Voyage Wellness Point – Business Cards</title>
<link rel="stylesheet" href="https://fonts.googleapis.com/css2?family=Open+Sans:wght@400;600&display=swap">
<style>
  :root {
    --page: #d6d6d6;
    --card: #1e1e1e;
    --card-edge: #2a2a2a;
    --accent: #f68d4d;
    --text-light: #f2f2f2;
    --text-muted: #b9b9b9;
    --map-tone: #2b2b2b;
    --line: #9a9a9a;
  }
  * { margin: 0; padding: 0; box-sizing: border-box; }
  html, body {
    width: 799px; height: 1200px; overflow: hidden;
    background: var(--page);
    font-family: "Open Sans", Arial, sans-serif;
  }
  .canvas { position: relative; width: 799px; height: 1200px; }
  .card {
    position: absolute; left: 60px; width: 680px; height: 389px;
    background: var(--card);
    border: 1px solid var(--card-edge);
    overflow: hidden;
  }
  .card--front { top: 150px; }
  .card--back { top: 660px; }

  .world-map {
    position: absolute; left: 210px; top: 40px; width: 360px; height: 230px;
    border-radius: 50% / 45%;
    background: radial-gradient(ellipse at center, var(--map-tone) 0%, rgba(43,43,43,0.6) 55%, rgba(30,30,30,0) 75%);
  }
  .brand-name {
    position: absolute; color: var(--accent); font-weight: 400; white-space: nowrap;
  }
  .card--front .brand-name { left: 0; right: 0; top: 112px; text-align: center; font-size: 48px; letter-spacing: 0.5px; }
  .tagline { position: absolute; color: var(--text-muted); font-size: 18px; white-space: nowrap; }
  .card--front .tagline { left: 0; right: 0; top: 182px; text-align: center; }

  .website {
    position: absolute; left: 0; right: 0; top: 300px;
    display: flex; align-items: center; justify-content: center; gap: 22px;
    font-size: 20px; color: var(--text-light);
  }
  .website .domain { color: var(--accent); }

  .card--back .brand-name { right: 40px; top: 92px; font-size: 34px; }
  .card--back .tagline { right: 42px; top: 142px; font-size: 15px; }

  .contact { position: absolute; left: 40px; top: 190px; }
  .contact .person { color: var(--accent); font-size: 26px; font-weight: 600; line-height: 1.1; }
  .contact .role { color: var(--text-light); font-size: 14px; margin-top: 2px; }
  .contact .rows { margin-top: 18px; }
  .contact .row { display: flex; align-items: center; gap: 12px; color: var(--text-light); font-size: 16px; line-height: 26px; }
  .contact .row svg { width: 16px; height: 16px; flex: none; }
  .flight-path { position: absolute; left: 0; top: 0; width: 680px; height: 389px; pointer-events: none; }
</style>
</head>
<body>
<div class="canvas">

  <section class="card card--front">
    <div class="world-map" role="img" aria-label="Faint world map backdrop"></div>
    <div class="brand-name">Voyage Wellness Point</div>
    <div class="tagline">Online Travel Health Experts</div>
    <div class="website">
      <svg width="64" height="12" viewBox="0 0 64 12" aria-hidden="true"><line x1="0" y1="6" x2="60" y2="6" stroke="var(--accent)" stroke-width="1.5"/><polyline points="54,1 61,6 54,11" fill="none" stroke="var(--accent)" stroke-width="1.5"/></svg>
      <span>www.<span class="domain">voyagewellpoint</span>.ca</span>
      <svg width="64" height="12" viewBox="0 0 64 12" aria-hidden="true"><line x1="4" y1="6" x2="64" y2="6" stroke="var(--accent)" stroke-width="1.5"/><polyline points="10,1 3,6 10,11" fill="none" stroke="var(--accent)" stroke-width="1.5"/></svg>
    </div>
  </section>

  <section class="card card--back">
    <div class="brand-name">Voyage Wellness Point</div>
    <div class="tagline">Online Travel Health Experts</div>

    <svg class="flight-path" viewBox="0 0 680 389" aria-hidden="true">
      <path d="M250 228 C 380 250, 470 300, 590 325" fill="none" stroke="var(--line)" stroke-width="1.5"/>
      <circle cx="596" cy="326" r="6" fill="var(--accent)"/>
    </svg>

    <div class="contact">
      <div class="person">Mara Kowalczyk</div>
      <div class="role">Managing Director</div>
      <div class="rows">
        <div class="row">
          <svg viewBox="0 0 16 16" aria-hidden="true"><path d="M3 2h3l1.5 3.5-2 1.2a8 8 0 0 0 3.8 3.8l1.2-2L14 10v3a1 1 0 0 1-1 1A11 11 0 0 1 2 3a1 1 0 0 1 1-1z" fill="var(--accent)"/></svg>
          <span>+1 555 283 0461</span>
        </div>
        <div class="row">
          <svg viewBox="0 0 16 16" aria-hidden="true"><rect x="1" y="3" width="14" height="10" fill="var(--accent)"/><polyline points="1,3 8,9 15,3" fill="none" stroke="var(--card)" stroke-width="1.3"/></svg>
          <span>mara@voyagewellpoint.ca</span>
        </div>
      </div>
    </div>
  </section>

</div>
</body>
</html>
```